Unique business card design

We are looking for a design that reflects our unique social media and online marketing agency "Kestrel Media". We are a young agency with a focus on speakers, coaches and trainers. In other words, we support people who want to do good with their work and help other people live a happier, more successful and fulfilling life, reach as many people as possible with their work and thus have an influence. Our values are: sustainability, creating added value, individuality, proactivity. We want our clients to feel comfortable with us and that's why the relationship with them is very important to us. We want every customer to become a lifelong friend of the company. Most of our clients are premium coaches, meaning they are in the higher priced segment and expect seriousness, professionalism and quality. All of these things should reflect our business card as well. I look forward to feedback. Best regards, Tomas Wylander

```html
<!DOCTYPE html>
<html lang="de">
<head>
<meta charset="utf-8">
<title>Kestrel Media – Business Card</title>
<link rel="stylesheet" href="https://fonts.googleapis.com/css2?family=Questrial&display=swap">
<style>
  :root {
    --stage: #000000;
    --card: #a3afb6;
    --ink: #1e1a5a;
    --accent: #1f4fa8;
  }
  html, body {
    margin: 0;
    padding: 0;
    width: 1200px;
    height: 1200px;
    overflow: hidden;
    background: var(--stage);
    font-family: "Questrial", "Century Gothic", sans-serif;
    color: var(--ink);
  }
  .stage {
    position: relative;
    width: 1200px;
    height: 1200px;
  }
  .card {
    position: absolute;
    background: var(--card);
  }
  .card--front { left: 197px; top: 202px; width: 393px; height: 682px; }
  .card--back  { left: 666px; top: 385px; width: 389px; height: 676px; }

  .brand {
    position: absolute;
    left: 0;
    right: 0;
    display: flex;
    justify-content: center;
    align-items: center;
    gap: 12px;
  }
  .card--front .brand { top: 140px; }
  .card--back .brand { top: 138px; }
  .brand__mark {
    width: 40px;
    height: 40px;
    background: var(--accent);
  }
  .brand__name {
    font-size: 30px;
    line-height: 1;
    color: var(--ink);
    white-space: nowrap;
  }

  .holder {
    position: absolute;
    top: 406px;
    left: 0;
    right: 0;
    text-align: center;
  }
  .holder__name {
    font-size: 25px;
    line-height: 30px;
  }
  .holder__role {
    font-size: 19px;
    line-height: 24px;
  }

  .contact {
    position: absolute;
    top: 486px;
    left: 64px;
    margin: 0;
    padding: 0;
    list-style: none;
  }
  .contact__item {
    display: flex;
    align-items: center;
    gap: 5px;
    height: 26px;
    font-size: 22px;
    line-height: 26px;
  }
  .contact__icon {
    width: 19px;
    height: 19px;
    flex: none;
    fill: var(--ink);
  }

  .values {
    position: absolute;
    top: 405px;
    left: 0;
    right: 0;
    margin: 0;
    padding: 0;
    list-style: none;
    text-align: center;
  }
  .values__item {
    font-size: 25px;
    line-height: 41px;
  }
</style>
</head>
<body>
<main class="stage">
  <section class="card card--front" aria-label="Card front">
    <div class="brand">
      <span class="brand__mark"></span>
      <span class="brand__name">Kestrel Media</span>
    </div>
    <div class="holder">
      <div class="holder__name">Tomas Wylander</div>
      <div class="holder__role">Your Designation</div>
    </div>
    <ul class="contact">
      <li class="contact__item">
        <svg class="contact__icon" viewBox="0 0 24 24" aria-hidden="true"><path d="M6.6 10.8c1.4 2.8 3.8 5.1 6.6 6.6l2.2-2.2c.3-.3.7-.4 1-.2 1.1.4 2.3.6 3.6.6.6 0 1 .4 1 1V20c0 .6-.4 1-1 1C10.6 21 3 13.4 3 4c0-.6.4-1 1-1h3.5c.6 0 1 .4 1 1 0 1.3.2 2.5.6 3.6.1.3 0 .7-.2 1z"/></svg>
        <span>123.456.7890</span>
      </li>
      <li class="contact__item">
        <svg class="contact__icon" viewBox="0 0 24 24" aria-hidden="true"><path d="M2 5h20v2l-10 6L2 7z"/><path d="M2 9l10 6 10-6v10H2z"/></svg>
        <span>youremail@email.com</span>
      </li>
      <li class="contact__item">
        <svg class="contact__icon" viewBox="0 0 24 24" aria-hidden="true"><path d="M12 2a10 10 0 1 0 0 20 10 10 0 0 0 0-20zm-1 17.9A8 8 0 0 1 4.1 11H7l2 2v2l2 2zm6.9-2.5c-.3-.8-1-1.4-1.9-1.4h-1v-3l-2-2H9V9h2l2-2V5.2a8 8 0 0 1 4.9 12.2z"/></svg>
        <span>yourwebsite.com</span>
      </li>
    </ul>
  </section>

  <section class="card card--back" aria-label="Card back">
    <div class="brand">
      <span class="brand__mark"></span>
      <span class="brand__name">Kestrel Media</span>
    </div>
    <ul class="values">
      <li class="values__item">Nachhaltigkeit</li>
      <li class="values__item">Mehrwert schaffen</li>
      <li class="values__item">Individualität</li>
      <li class="values__item">Proaktivität</li>
    </ul>
  </section>
</main>
</body>
</html>
```